Harrowgate Estates Business Card for Apartment Buildings

Create business cards for resident managers who run apartment buildings. The audience is the public who are searching for apartment rentals, and current residents who live at the apartment building. Key design element will be incorporating the company logo, however, the logo cannot dominate. The building name and manager name are more important than the logo. Current business card design leaves little room for copy, so we may need to reduce the size on the current card to allow for more space for copy.

Target Market(s)

Adults 18-65 years of age, who are looking for an apartment rental, plus current residents who live at our apartment buildings.

Industry/Entity Type

Property Management

Contact Information for Business Card

A major design element will be use of the company logo. Important property and manager contact information must be part of the design. The size of the logo will need to be reduced to make room for building and manager contact copy.

Font styles to use
Sans Serif

Colors
3176b5
000000
959595
ffffff

Requirements
Must have
• 1) Incorporate the company logo.
• 2) Use the company colors (dark blue, black/grey, over white).
• 3) FEATURE THE BUILDING NAME
• 4) FEATURE THE MANAGER NAME
• 5) The company name is less important than BUILDING and MANAGER
• 6) Manager contact information
• **SEE ATTACHED CREATIVE BRIEF**
Nice to have
• 1) Back of card logo watermark
• 2) Ability to write notes on back of carfd
Should not have
• Avoid letting the company logo dominate the card, the building name and manager are more important than the company logo.

```html
<!DOCTYPE html>
<html lang="en">
<head>
<meta charset="utf-8">
<title>Harrowgate Estates – Business Card</title>
<link rel="stylesheet" href="https://fonts.googleapis.com/css2?family=PT+Sans:wght@400;700&display=swap">
<style>
  :root {
    --brand-blue: #3176b5;
    --ink: #000000;
    --charcoal: #444548;
    --mid-grey: #959595;
    --rule-grey: #6f6f6f;
    --paper: #ffffff;
    --backdrop: #e8e8e6;
  }
  * { box-sizing: border-box; margin: 0; padding: 0; }
  html, body { width: 1200px; height: 800px; overflow: hidden; }
  body {
    background: var(--backdrop);
    font-family: "PT Sans", sans-serif;
    color: var(--charcoal);
  }
  .canvas {
    position: relative;
    width: 1200px;
    height: 800px;
    display: flex;
    align-items: center;
    justify-content: center;
    gap: 40px;
  }
  .card {
    position: relative;
    width: 540px;
    height: 309px;
    background: var(--paper);
    box-shadow: 0 6px 18px rgba(0,0,0,0.12);
    overflow: hidden;
  }

  /* ---------- Back: notes side ---------- */
  .notes-lines {
    position: absolute;
    left: 34px;
    right: 34px;
    top: 34px;
    display: flex;
    flex-direction: column;
    gap: 25px;
  }
  .notes-lines span {
    display: block;
    height: 1px;
    background: var(--rule-grey);
  }
  .tab {
    position: absolute;
    width: 22px;
    height: 118px;
    border-radius: 0 0 0 0;
  }
  .tab--top-right {
    right: 0;
    top: 22px;
    background: var(--charcoal);
    border-radius: 14px 0 0 14px;
  }
  .tab--bottom-left {
    left: 0;
    bottom: 22px;
    background: var(--brand-blue);
    border-radius: 0 14px 14px 0;
  }

  /* ---------- Front: contact side ---------- */
  .brand-name {
    position: absolute;
    left: 38px;
    top: 36px;
    font-size: 25px;
    font-weight: 700;
    color: var(--brand-blue);
    letter-spacing: 0.3px;
    text-transform: uppercase;
  }
  .manager-band {
    position: absolute;
    right: 0;
    top: 84px;
    width: 250px;
    height: 66px;
    background: var(--brand-blue);
    clip-path: polygon(0 0, 100% 0, 100% 100%, 8% 100%);
    color: var(--paper);
    text-align: right;
    padding: 11px 16px 0 0;
  }
  .manager-name {
    font-size: 20px;
    font-weight: 700;
    letter-spacing: 0.3px;
    line-height: 1.1;
    text-transform: uppercase;
  }
  .manager-title {
    font-size: 15px;
    font-weight: 400;
    line-height: 1.3;
  }
  .contact-list {
    position: absolute;
    left: 38px;
    top: 128px;
    list-style: none;
    font-size: 12.5px;
    color: var(--charcoal);
  }
  .contact-list li {
    display: flex;
    align-items: center;
    gap: 10px;
    height: 17px;
  }
  .contact-list li.gap-after { margin-bottom: 9px; }
  .contact-list svg { width: 11px; height: 11px; fill: var(--brand-blue); flex: none; }
  .address-band {
    position: absolute;
    left: 0;
    top: 230px;
    width: 430px;
    height: 24px;
    background: var(--charcoal);
    clip-path: polygon(0 0, 96% 0, 100% 100%, 0 100%);
    color: var(--paper);
    font-size: 12.5px;
    line-height: 24px;
    padding-left: 22px;
  }
</style>
</head>
<body>
<main class="canvas">

  <!-- Back of card: notes area -->
  <section class="card card--back" aria-label="Back of card with lines for notes">
    <div class="tab tab--top-right"></div>
    <div class="tab tab--bottom-left"></div>
    <div class="notes-lines">
      <span></span><span></span><span></span><span></span><span></span>
      <span></span><span></span><span></span><span></span>
    </div>
  </section>

  <!-- Front of card: manager contact -->
  <section class="card card--front" aria-label="Front of business card">
    <div class="brand-name">Harrowgate Estates</div>

    <div class="manager-band">
      <div class="manager-name">Daniel Ashworth</div>
      <div class="manager-title">Property Manager</div>
    </div>

    <ul class="contact-list">
      <li>
        <svg viewBox="0 0 24 24" aria-hidden="true"><path d="M6.6 10.8a15 15 0 0 0 6.6 6.6l2.2-2.2c.3-.3.7-.4 1-.2 1.1.4 2.3.6 3.6.6.6 0 1 .4 1 1V20c0 .6-.4 1-1 1A17 17 0 0 1 3 4c0-.6.4-1 1-1h3.5c.6 0 1 .4 1 1 0 1.3.2 2.5.6 3.6.1.3 0 .7-.2 1z"/></svg>
        555-314-0192
      </li>
      <li class="gap-after">
        <svg viewBox="0 0 24 24" aria-hidden="true"><path d="M6 2h12v6H6zM3 9h18a1 1 0 0 1 1 1v7h-4v5H6v-5H2v-7a1 1 0 0 1 1-1zm5 7v4h8v-4z"/></svg>
        555-314-0247
      </li>
      <li>
        <svg viewBox="0 0 24 24" aria-hidden="true"><path d="M2 5h20v14H2zm2 2v.5l8 5 8-5V7z"/></svg>
        daniel@harrowgateestates.us
      </li>
      <li>
        <svg viewBox="0 0 24 24" aria-hidden="true"><path d="M12 2a10 10 0 1 0 0 20 10 10 0 0 0 0-20zm6.9 9h-3a15 15 0 0 0-1.3-6A8 8 0 0 1 18.9 11zM12 4.1c.9 1.3 1.7 3.6 1.9 6.9h-3.8c.2-3.3 1-5.6 1.9-6.9zM9.4 5a15 15 0 0 0-1.3 6h-3A8 8 0 0 1 9.4 5zm-4.3 8h3a15 15 0 0 0 1.3 6 8 8 0 0 1-4.3-6zm6.9 6.9c-.9-1.3-1.7-3.6-1.9-6.9h3.8c-.2 3.3-1 5.6-1.9 6.9zm2.6-.9a15 15 0 0 0 1.3-6h3a8 8 0 0 1-4.3 6z"/></svg>
        www.harrowgateestates.us
      </li>
    </ul>

    <div class="address-band">1270 Alder Creek Road #B210, Fairview, CA 90412</div>
  </section>

</main>
</body>
</html>
```